Church needs an introductory/informative postcard

We are looking for a postcard that would introduce our church along with having our programing information. We need it to be in Spanish, I can provide the necessary translation. Please provide us with ideas for a tag line that invites people to come check us out. We can provide a bible scripture if necessary, but would like something short that projects interest and confidence. We have a logo that we would like incorporated.

Target Market(s)

Hispanic

Industry/Entity Type

Religious

Requirements
Must have
• Colorful to coordinate with our logo so it flows well
• Have an tag line that invites people to our church
Nice to have
• have a modern feel
• if needed we can provide some pictures of our building
Should not have
• Pictures of people

```html
<!DOCTYPE html>
<html lang="es">
<head>
<meta charset="utf-8">
<title>Monte Sion – Postal</title>
<link rel="stylesheet" href="https://fonts.googleapis.com/css2?family=Cinzel:wght@400;700;900&family=Jost:ital,wght@0,400;0,500;1,400&display=swap">
<style>
  :root{
    --bg:#d9d9d9;
    --card:#ffffff;
    --ink:#1c1c1c;
    --purple:#5b2a86;
    --orange:#e0401c;
    --blue:#29a9e1;
    --green:#8cc63f;
    --paper-light:#e9e4cf;
    --paper-mid:#d8d1b4;
    --photo-dark:#6d6658;
    --panel-light:#ffffff;
    --panel-grey:#e4e4e4;
  }
  *{box-sizing:border-box;margin:0;padding:0}
  html,body{width:900px;height:1200px;overflow:hidden}
  body{background:var(--bg);position:relative;font-family:"Jost",sans-serif;color:var(--ink)}
  .postcard{position:absolute;left:105px;width:690px;height:530px;background:var(--card);overflow:hidden;box-shadow:0 4px 14px rgba(0,0,0,.25)}
  .postcard--front{top:53px}
  .postcard--back{top:628px}

  /* front */
  .front-photo{position:absolute;inset:0;background:
      linear-gradient(90deg,var(--photo-dark) 0%,#9a8f76 28%,var(--paper-mid) 50%,var(--paper-light) 100%)}
  .brand-name{font-family:"Cinzel",serif;font-weight:700;color:var(--purple);letter-spacing:.5px}
  .front-brand{position:absolute;right:45px;top:72px;text-align:right}
  .front-brand .brand-mark{display:block;width:46px;height:46px;border-radius:50%;background:var(--purple);margin:0 0 10px auto}
  .front-brand .brand-name{font-size:24px}
  .tagline{position:absolute;right:42px;top:174px;text-align:right;font-family:"Cinzel",serif}
  .tagline__lead{font-size:25px;color:var(--ink);line-height:34px}
  .tagline__accent{font-size:27px;font-weight:700;color:var(--purple);line-height:40px}
  .scripture{position:absolute;right:35px;top:334px;text-align:right;font-style:italic;font-size:18px;line-height:25px;color:var(--ink)}
  .scripture__ref{position:absolute;right:35px;top:486px;font-style:italic;font-size:18px}
  .front-web{position:absolute;left:218px;top:492px;font-family:"Cinzel",serif;font-size:12px;color:var(--orange)}

  /* back */
  .back-panel{position:absolute;left:0;top:0}
  .info{position:absolute;left:35px;top:22px;width:300px}
  .info__kicker{font-family:"Cinzel",serif;font-size:19px;line-height:24px}
  .info__headline{font-family:"Cinzel",serif;font-weight:700;font-size:24px;line-height:30px}
  .info__rule{width:270px;height:1px;background:var(--blue);margin:6px 0 10px}
  .info__label{font-family:"Cinzel",serif;font-size:18px;color:var(--orange);line-height:24px}
  .info__label--bold{font-weight:700}
  .info__text{font-size:17px;line-height:23px}
  .gap-s{margin-top:6px}
  .gap-m{margin-top:14px}
  .schedule{list-style:none;margin-top:4px}
  .schedule li{font-family:"Cinzel",serif;font-weight:700;font-size:13px;line-height:21.5px}
  .schedule time{color:var(--blue)}
  .phone{font-family:"Cinzel",serif;font-weight:700;font-size:18px;line-height:24px}
  .social{display:flex;align-items:center;gap:12px;margin-top:12px}
  .social .info__label{font-size:15px;margin-right:26px}
  .social__slot{width:18px;height:18px;border-radius:3px;background:var(--ink)}
  .back-web{font-size:13px;color:var(--blue);margin-top:6px}
  .back-brand{position:absolute;left:425px;top:22px;width:100px;text-align:center}
  .back-brand .brand-mark{display:block;width:40px;height:40px;border-radius:50%;background:var(--purple);margin:0 auto 14px}
  .back-brand .brand-name{font-size:16px;white-space:nowrap}
  .stamp-box{position:absolute;left:577px;top:30px;width:82px;height:87px;border:1.5px solid var(--ink)}
</style>
</head>
<body>

<section class="postcard postcard--front">
  <div class="front-photo" role="img" aria-label="Fotografía: persona con camisa de mezclilla sosteniendo una Biblia abierta sobre fondo claro"></div>
  <div class="front-brand">
    <span class="brand-mark"></span>
    <span class="brand-name">MONTE SION</span>
  </div>
  <div class="tagline">
    <div class="tagline__lead">We're saving a place</div>
    <div class="tagline__accent">JUST FOR YOU !</div>
  </div>
  <p class="scripture">Así que somos embajadores de<br>Cristo, como si Dios los exhortara a<br>ustedes por medio de nosotros:<br>En nombre de Cristo les rogamos<br>que se reconcilien con Dios.</p>
  <span class="front-web">www.iglesiamontesion.org</span>
  <span class="scripture__ref">II Coríntos 5:20</span>
</section>

<section class="postcard postcard--back">
  <svg class="back-panel" width="690" height="530" viewBox="0 0 690 530" aria-hidden="true">
    <defs>
      <linearGradient id="panelFade" x1="0" y1="0" x2="1" y2="0">
        <stop offset="0" stop-color="var(--panel-grey)"/>
        <stop offset=".5" stop-color="var(--panel-light)"/>
        <stop offset="1" stop-color="var(--panel-grey)"/>
      </linearGradient>
    </defs>
    <path d="M0,0 H282 C350,40 380,110 362,200 C345,290 268,350 292,420 C300,445 312,458 322,465 H0 Z" fill="url(#panelFade)"/>
    <path d="M287,465 C255,400 292,340 330,280 C355,240 360,215 362,200 C358,300 300,360 322,465 Z" fill="var(--purple)"/>
    <path d="M282,0 C350,40 380,110 362,200 C345,290 268,350 292,420" fill="none" stroke="var(--orange)" stroke-width="9"/>
    <path d="M298,0 C368,40 396,112 376,205 C360,285 300,340 305,395" fill="none" stroke="var(--blue)" stroke-width="9"/>
  </svg>

  <div class="info">
    <div class="info__kicker">Where can God</div>
    <div class="info__headline">USE YOUR TALENTS?</div>
    <div class="info__rule"></div>
    <div class="info__label">ENVÍANOS EMAIL</div>
    <div class="info__text gap-s">info@iglesiamontesion.org</div>
    <div class="info__label gap-s">LLÁMANOS</div>
    <div class="info__text gap-s">2045 Linden Ave.<br>Meadowvale, TX 75099</div>
    <div class="info__label info__label--bold gap-m">SERVICIOS:</div>
    <ul class="schedule">
      <li>DOMINGO <time>10:00 AM</time></li>
      <li>LUNES <time>7:00 PM</time></li>
      <li>MIÉRCOLES <time>7:00 PM</time></li>
    </ul>
    <div class="info__label info__label--bold gap-m">TELÉFONO:</div>
    <div class="phone">555.014.2287</div>
    <div class="social">
      <span class="info__label">SÍGUENOS</span>
      <span class="social__slot"></span>
      <span class="social__slot"></span>
      <span class="social__slot"></span>
    </div>
    <div class="back-web">www.iglesiamontesion.org</div>
  </div>

  <div class="back-brand">
    <span class="brand-mark"></span>
    <span class="brand-name">MONTE SION</span>
  </div>
  <div class="stamp-box"></div>
</section>

</body>
</html>
```